Logo & Business Card Design for Law Firm
Harlow Law Group
Logo & Business Card Design for Law Firm - Law
Creative Brief
Trial Lawyers
I am looking for a bold logo and business card design for a start-up law firm based in Philadelphia and with offices in PA and NJ. Harlow Law Group is led by trial attorneys and specializes in catastrophic personal injury litigation stemming from construction / industrial accidents, truck/auto accidents, defective products, falls, and medical malpractice.
I am looking for a design that displays an image that is modern, clean, and somewhat minimalist while at the same time conveys that the Harlow Law Group brand is serious. I am not looking for some hokey integration of the scales of justice or anything along those played-out lines. The color palate for the design is flexible; however, I am partial to blues, greens, and reds.
For the business card, I am looking for something that is dual-sided. The front should display the logo, attorney name (with Trial Lawyer as the title beneath the name - use Derek T. Harlow, as the name for the sample), address (2700 Bramble Avenue, 32nd Floor, Philadelphia, PA 19104), phone, fax, and website (www.harlowtrialfirm.example). If there is room, I may also add my NJ office location - assuming it doesn't overload the image. The back of the card should list my areas of expertise: Serious Injuries / Wrongful Death, Brain Injuries, Construction Accidents, Industrial Accidents, Truck Accidents, Car Accidents, Defective Products, Electrocution Injuries, Burn Injuries, Slip/Trip and Falls, and Commercial Litigation.
Professional
Color selection is flexible; however, I tend to prefer blues, greens, and reds.

```html
<!DOCTYPE html>
<html lang="en">
<head>
<meta charset="utf-8">
<title>Harlow Law Group – Business Card Back</title>
<link href="https://fonts.googleapis.com/css2?family=Questrial&display=swap" rel="stylesheet">
<style>
  :root {
    --page-bg: #f2f3f5;
    --card-bg: #ffffff;
    --card-edge: #e3e6ea;
    --ink: #1e1e1e;
    --brand-blue: #1f6fb8;
    --soft-blue: #dfe7f2;
  }
  * { margin: 0; padding: 0; box-sizing: border-box; }
  html, body {
    width: 1200px;
    height: 898px;
    overflow: hidden;
    background: var(--page-bg);
    font-family: "Questrial", "Century Gothic", sans-serif;
  }
  .canvas {
    position: relative;
    width: 1200px;
    height: 898px;
  }
  .card {
    position: absolute;
    left: 100px;
    top: 163px;
    width: 1000px;
    height: 572px;
    background: linear-gradient(160deg, var(--card-bg) 55%, #f6f8fb 100%);
    border: 1px solid var(--card-edge);
    box-shadow: 0 18px 40px rgba(0, 0, 0, 0.12);
  }
  .brand {
    position: absolute;
    left: 70px;
    top: 246px;
    display: flex;
    align-items: center;
    gap: 18px;
  }
  .brand-dot {
    width: 34px;
    height: 34px;
    border-radius: 50%;
    background: var(--brand-blue);
  }
  .brand-name {
    font-size: 40px;
    color: var(--brand-blue);
    letter-spacing: 0.5px;
  }
  .practice-areas {
    position: absolute;
    right: 52px;
    top: 58px;
    list-style: none;
    text-align: right;
    font-size: 26px;
    line-height: 41px;
    color: var(--ink);
  }
  .practice-areas li::before {
    content: "~ ";
  }
</style>
</head>
<body>
<main class="canvas">
  <section class="card" aria-label="Business card back – areas of practice">
    <div class="brand">
      <span class="brand-dot"></span>
      <span class="brand-name">Harlow Law Group</span>
    </div>
    <ul class="practice-areas">
      <li>Serious Injuries</li>
      <li>Wrongful Death,</li>
      <li>Brain Injuries,</li>
      <li>Construction Accidents,</li>
      <li>Industrial Accidents,</li>
      <li>Truck Accidents,</li>
      <li>Car Accidents,</li>
      <li>Defective Products,</li>
      <li>Electrocution Injuries,</li>
      <li>Burn Injuries,</li>
      <li>Slip/Trip and Falls</li>
      <li>and Commercial Litigation</li>
    </ul>
  </section>
</main>
</body>
</html>
```